Fish Farm needing 3 - Fold Flyer / Price List designed

We are looking for a new Price List for our Fish Farm. I have attached an example of the basic info that needs in the flyer. We want the flyer to be a 3 fold page. Anything that is on our website, you can use for ideas. There are some pictures on there that can be photoshopped into the flyer. Do not use any photos from any other sites. We are looking for something professional but fun and exciting! I have also attached our business logo. We tend to stay with the blues and greens for colors. Let's get started....
Updates

Need extra days to review

Contact Information for Business Card

We are needing a business card with our new logo on it. We also need our address, phone numbers, email address, and website listed. Please view our website for more ideas.

Colors

```html
<!DOCTYPE html>
<html lang="en">
<head>
<meta charset="utf-8">
<title>Harlow's Fish Farm – Tri-fold Price List</title>
<link href="https://fonts.googleapis.com/css2?family=Exo+2:wght@600;700&family=Open+Sans:wght@400;600&display=swap" rel="stylesheet">
<style>
  :root {
    --navy: #2c2f9c;
    --accent: #1f7ad6;
    --paper: #f6f6f8;
    --panel-grey: #e4e5ea;
    --backdrop: #e8e8eb;
    --ink: #1d1d24;
    --white: #ffffff;
  }
  html, body {
    margin: 0;
    width: 1200px;
    height: 1121px;
    overflow: hidden;
    background: var(--backdrop);
  }
  .brochure {
    position: absolute;
    left: 48px;
    top: 166px;
    width: 1104px;
    height: 789px;
    background: var(--paper);
    box-shadow: 0 6px 22px rgba(0,0,0,.25);
    font-family: "Open Sans", sans-serif;
    color: var(--ink);
  }
  .brochure-art {
    position: absolute;
    inset: 0;
  }
  .text { position: absolute; margin: 0; }

  /* left panel */
  .call-note {
    left: 20px; top: 36px; width: 340px;
    color: var(--white); font-size: 14.5px; font-weight: 600; line-height: 1.3;
  }
  .delivery-note {
    right: 740px; top: 598px; width: 320px; text-align: right;
    color: var(--white); font-size: 14px; font-weight: 600; line-height: 1.35;
  }
  .schedule-note {
    right: 740px; top: 672px; width: 340px; text-align: right;
    color: var(--white); font-size: 14px; font-weight: 600; line-height: 1.35;
  }
  .schedule-url {
    right: 740px; top: 724px; text-align: right; white-space: nowrap;
    color: var(--white); font-size: 19px; font-weight: 600;
  }

  /* brand name */
  .brand-name {
    font-family: "Exo 2", sans-serif; font-weight: 700;
    color: var(--navy); letter-spacing: .5px; white-space: nowrap;
  }
  .brand-middle { left: 375px; width: 364px; top: 290px; text-align: center; font-size: 29px; }
  .brand-cover { left: 739px; width: 365px; top: 48px; text-align: center; font-size: 30px; }

  /* middle panel */
  .rates-title {
    left: 394px; top: 388px;
    font-family: "Exo 2", sans-serif; font-weight: 700; font-size: 21px; line-height: 1.1;
    color: var(--navy); text-transform: uppercase;
  }
  .rates-unit {
    left: 394px; top: 442px;
    font-family: "Exo 2", sans-serif; font-weight: 600; font-size: 15px;
  }
  .rates-list {
    left: 390px; top: 477px; list-style: none; padding: 0;
    font-size: 12.5px; line-height: 18px;
  }

  /* cover panel */
  .farm-address {
    left: 739px; width: 365px; top: 112px; text-align: center;
    font-family: "Exo 2", sans-serif; font-weight: 600; font-size: 13.5px; line-height: 16px;
  }
  .farm-contacts {
    left: 739px; width: 365px; top: 158px; text-align: center;
    font-size: 11px; line-height: 15.5px; list-style: none; padding: 0;
  }
  .farm-contacts .label { color: var(--accent); }

  .price-title {
    left: 763px; top: 612px;
    font-family: "Exo 2", sans-serif; font-weight: 700; font-size: 25px;
    color: var(--white); letter-spacing: .5px;
  }
  .price-list {
    left: 763px; top: 656px; width: 330px;
    display: grid; grid-template-columns: 138px 1fr; grid-auto-flow: column;
    grid-template-rows: repeat(6, 18px);
    list-style: none; padding: 0;
    color: var(--white); font-size: 11.5px; text-transform: uppercase;
  }
  .price-list li::before {
    content: ""; display: inline-block; width: 6px; height: 6px; border-radius: 50%;
    background: var(--white); margin: 0 9px 1px 0; vertical-align: middle;
  }
</style>
</head>
<body>
<main class="brochure">
  <svg class="brochure-art" viewBox="0 0 1104 789" width="1104" height="789">
    <defs>
      <linearGradient id="panel-shade" x1="0" x2="1">
        <stop offset="0" stop-color="#ffffff"/>
        <stop offset="1" stop-color="#e2e3e8"/>
      </linearGradient>
      <linearGradient id="pond-photo" x1="0" y1="0" x2="1" y2="1">
        <stop offset="0" stop-color="#8a8a6a"/>
        <stop offset=".6" stop-color="#a79f86"/>
        <stop offset="1" stop-color="#5f7a3c"/>
      </linearGradient>
      <linearGradient id="angler-photo" x1="0" y1="0" x2="0" y2="1">
        <stop offset="0" stop-color="#5e8a3e"/>
        <stop offset=".5" stop-color="#8fa66c"/>
        <stop offset="1" stop-color="#c9cfc2"/>
      </linearGradient>
    </defs>

    <rect class="panel-bg" x="375" y="0" width="364" height="789" fill="url(#panel-shade)"/>
    <rect class="panel-bg" x="739" y="0" width="365" height="789" fill="#f1f1f4"/>

    <g role="img" aria-label="Photo of a farmer holding a large bass beside a pond">
      <rect x="739" y="240" width="365" height="360" fill="url(#angler-photo)"/>
    </g>
    <g role="img" aria-label="Photo of a farmer pulling a seine net through a pond">
      <rect x="375" y="555" width="364" height="234" fill="url(#pond-photo)"/>
    </g>
    <g role="img" aria-label="Road map showing the route to the farm">
      <rect x="60" y="215" width="255" height="330" fill="#ecedf2"/>
    </g>

    <!-- top band, left and middle panels -->
    <path d="M0,0 H613 C655,60 700,125 739,170 V248 C560,150 330,70 0,172 Z" fill="var(--navy)"/>
    <path d="M0,192 C260,95 520,150 739,268" fill="none" stroke="var(--accent)" stroke-width="8"/>

    <!-- cover wave -->
    <path d="M739,238 C860,250 1000,236 1104,214 V248 C1000,266 860,272 739,272 Z" fill="var(--navy)"/>
    <path d="M739,280 C860,280 1000,270 1104,256" fill="none" stroke="var(--accent)" stroke-width="5"/>

    <!-- bottom bands -->
    <path d="M0,702 C120,622 260,576 375,566 V789 H0 Z" fill="var(--navy)"/>
    <path d="M0,684 C120,604 260,560 375,552 C520,543 640,556 739,590" fill="none" stroke="var(--accent)" stroke-width="6"/>
    <path d="M739,602 C880,602 1000,588 1104,562 V789 H739 Z" fill="var(--navy)"/>
    <path d="M739,590 C880,590 1000,576 1104,548" fill="none" stroke="var(--accent)" stroke-width="6"/>
  </svg>

  <!-- left panel -->
  <p class="text call-note">Feel free to call the farm or the cell phone. If no answer, leave a message and we will get back to you as soon as possible.</p>
  <p class="text delivery-note">Always call before coming<br>to the farm as we may be<br>on a delivery.</p>
  <p class="text schedule-note">Our Sales Route Schedule is listed<br>on our website at:</p>
  <p class="text schedule-url">www.harlowsfishfarm.com/schedule</p>

  <!-- middle panel -->
  <p class="text brand-name brand-middle">HARLOW'S FISH FARM</p>
  <h2 class="text rates-title">Standard Stocking<br>Rates</h2>
  <p class="text rates-unit">Per Surface Acre</p>
  <ul class="text rates-list">
    <li>600-1,000..........Hybrid Bluegill, Regular Bluegill, or Redear</li>
    <li>100-200 ............Largemouth Bass</li>
    <li>100-200............Channel Catfish</li>
    <li>3,000-5,000...... Fathead Minnows</li>
  </ul>

  <!-- cover panel -->
  <h1 class="text brand-name brand-cover">HARLOW'S FISH FARM</h1>
  <p class="text farm-address">4180 E. Heron Lake Rd.<br>Millbrook, IN 47000</p>
  <ul class="text farm-contacts">
    <li><span class="label">Farm:</span> (555) 210-4471</li>
    <li><span class="label">Cell:</span> (555) 318-2096</li>
    <li><span class="label">Text:</span> (555) 402-7733</li>
    <li>harlowsfishfarm@pondmail.net</li>
    <li>www.harlowsfishfarm.com</li>
  </ul>

  <h2 class="text price-title">2019 PRICE LIST FOR:</h2>
  <ul class="text price-list">
    <li>Hybrid Bluegill</li>
    <li>Regular Bluegill</li>
    <li>Redear Sunfish</li>
    <li>Largemouth Bass</li>
    <li>Fathead Minnows</li>
    <li>Golden Shiners</li>
    <li>Triploid Grass Carp</li>
    <li>Channel Catfish</li>
    <li>Albino Catfish</li>
    <li>Black Crappie</li>
    <li>Japanese Koi</li>
    <li>Tilapia, Fish Food</li>
  </ul>
</main>
</body>
</html>
```